Slick Quillnest Ad

We've recently re-branded our business to reflect our ethos "Wealth is about more than money - it's about choice." We aim to protect your hard-earned success and help achieve your lifestyle aspirations, whether that's retiring at fifty to go globetrotting, or buying your first home. We're a financial consultancy that primarily services high-net-worth clients.

Our brand is minimalist, modern (check out our website) and the brief focuses on our strong investment return for the past 12 years.

Task: The attached brief is for a Quillnest advertisement. Please see competitor images as a guide to how 'returns' and 'branding' can both be displayed in a design.

Target Market(s)

+30

Font styles to use
Sans Serif

Requirements
Must have
• Creative should feature the strong investment return, and design aesthetic should be 'on-brand' (modern, minimalist, lifestyle focused).

```html
<!DOCTYPE html>
<html lang="en">
<head>
<meta charset="utf-8">
<title>Quillnest – Global Investment Portfolio Returns</title>
<link href="https://fonts.googleapis.com/css2?family=Mulish:wght@600;700;800;900&display=swap" rel="stylesheet">
<style>
  :root {
    --paper: #ffffff;
    --olive: #a9b000;
    --olive-deep: #5e6214;
    --ink: #232527;
    --body-grey: #4a4d52;
    --muted-grey: #6e7480;
    --silver-light: #d3d7de;
    --silver-dark: #8d929b;
    --chart-lime: #d8e65a;
    --chart-grey: #b9bec6;
  }
  html, body {
    margin: 0;
    padding: 0;
    width: 1200px;
    height: 1200px;
    overflow: hidden;
    background: var(--paper);
  }
  .ad {
    position: relative;
    width: 1200px;
    height: 1200px;
    background: var(--paper);
    font-family: "Mulish", Arial, sans-serif;
    overflow: hidden;
  }
  .trend {
    position: absolute;
    inset: 0;
    width: 1200px;
    height: 1200px;
    pointer-events: none;
  }
  .figure {
    position: absolute;
    margin: 0;
    font-weight: 900;
    line-height: 1;
    white-space: nowrap;
    background-clip: text;
    -webkit-background-clip: text;
    color: transparent;
    -webkit-text-fill-color: transparent;
  }
  .figure .pct { font-weight: 800; }
  .figure--portfolio {
    left: 112px;
    top: 140px;
    font-size: 430px;
    letter-spacing: -22px;
    background-image: linear-gradient(100deg, var(--olive) 0%, var(--olive) 30%, var(--olive-deep) 52%, var(--ink) 66%, var(--ink) 100%);
  }
  .figure--portfolio .pct { font-size: 240px; letter-spacing: 0; margin-left: 18px; }
  .figure--index {
    left: 312px;
    top: 700px;
    font-size: 360px;
    letter-spacing: -16px;
    background-image: linear-gradient(100deg, var(--silver-light) 0%, var(--silver-dark) 70%, var(--silver-dark) 100%);
  }
  .figure--index .pct { font-size: 200px; letter-spacing: 0; margin-left: 14px; }
  .headline {
    position: absolute;
    left: 352px;
    top: 515px;
    margin: 0;
    font-size: 41px;
    font-weight: 700;
    line-height: 1.22;
    color: var(--body-grey);
  }
  .index-label {
    position: absolute;
    left: 352px;
    top: 688px;
    margin: 0;
    font-size: 40px;
    font-weight: 700;
    color: var(--muted-grey);
  }
  .brand {
    position: absolute;
    right: 62px;
    bottom: 110px;
    display: flex;
    align-items: center;
    gap: 14px;
  }
  .brand-dot {
    width: 30px;
    height: 30px;
    border-radius: 50%;
    border: 4px solid var(--olive);
    box-sizing: border-box;
  }
  .brand-name {
    font-size: 38px;
    font-weight: 800;
    color: var(--olive);
  }
</style>
</head>
<body>
<main class="ad">
  <svg class="trend" viewBox="0 0 1200 1200" aria-hidden="true">
    <polyline fill="none" stroke="var(--chart-lime)" stroke-width="5" stroke-opacity="0.8" stroke-linejoin="round"
      points="95,450 120,445 135,470 150,505 170,520 190,500 210,470 225,480 240,455 255,465 270,450 285,470 300,445 320,440 335,465 350,440 365,470 380,430 395,470 410,445 425,455 445,435 460,450 470,430 485,470 500,450 515,440 530,420 545,400 560,380 575,385 590,365 605,345 620,310 635,290 650,275 665,265 680,262 695,255 710,250 725,240 735,215 745,190 760,170 775,160 790,150 805,148 820,160 835,162 850,150 865,125 875,100"/>
    <polyline fill="none" stroke="var(--chart-lime)" stroke-width="2" stroke-opacity="0.55"
      points="95,460 120,455 135,485 150,515 170,530 190,510 210,480 225,492 240,466 255,476 270,462 285,480 300,456 320,452 335,476 350,452 365,482 380,442 395,482 410,456 425,466 445,446 460,462 470,442 485,480"/>
    <polyline fill="none" stroke="var(--chart-grey)" stroke-width="3" stroke-opacity="0.6" stroke-linejoin="round"
      points="130,935 145,905 160,960 175,900 190,950 205,905 220,960 235,910 250,945 265,920 280,960 295,905 310,955 325,915 340,950 355,905 370,940 385,915 400,955 415,920 430,935 445,925 460,955 475,935 490,960 505,930 520,960 535,935 550,965 565,960 580,925 595,950 610,935 625,945 640,905 655,880 670,840 685,830 700,835 715,820 730,825 745,810 760,815 775,800 790,805 805,790 815,760 825,730 835,745 845,775 855,790 870,760 885,770 900,795 915,780 930,770"/>
    <polyline fill="none" stroke="var(--chart-grey)" stroke-width="2" stroke-opacity="0.35"
      points="130,945 145,915 160,970 175,910 190,960 205,915 220,970 235,920 250,955 265,930 280,970 295,915 310,965"/>
  </svg>

  <h1 class="figure figure--portfolio">20.3<span class="pct">%</span></h1>
  <p class="headline">Our Global Investment Portfolio<br>outperformed the AXI by 10.8%</p>

  <p class="index-label">The AXI Returned.</p>
  <p class="figure figure--index">9.5<span class="pct">%</span></p>

  <div class="brand">
    <span class="brand-dot"></span>
    <span class="brand-name">Quillnest</span>
  </div>
</main>
</body>
</html>
```